Business Card Design Project

Business Card
We are rebranding with a new logo
Industry/Entity Type
Business
Contact Information for Business Card
Dennis Marlow +61 427581962 dennis@qovo.com.au P.O. Box 872 Kelvindale QLD 4309
Requirements
Must have
- Logo

```html
<!DOCTYPE html>
<html lang="en">
<head>
<meta charset="utf-8">
<title>Qovo International – Business Card</title>
<link rel="stylesheet" href="https://fonts.googleapis.com/css2?family=Montserrat:wght@400;700&display=swap">
<style>
  :root {
    --page-bg: #e9ecef;
    --card-bg: #ffffff;
    --brand-orange: #ee7d1a;
    --brand-navy: #1d5e84;
    --text-blue: #2b6b91;
    --panel-light: #1f9ad6;
    --panel-deep: #0a6198;
  }
  html, body {
    margin: 0;
    padding: 0;
    width: 1200px;
    height: 840px;
    overflow: hidden;
    background: var(--page-bg);
  }
  .canvas {
    width: 1200px;
    height: 840px;
    display: flex;
    align-items: center;
    justify-content: center;
  }
  .business-card {
    position: relative;
    width: 900px;
    height: 550px;
    background: var(--card-bg);
    overflow: hidden;
    box-shadow: 0 10px 30px rgba(0, 0, 0, 0.12);
    font-family: "Montserrat", sans-serif;
  }
  .brand-name {
    position: absolute;
    left: 56px;
    top: 92px;
    margin: 0;
    font-size: 30px;
    font-weight: 700;
    color: var(--brand-orange);
    letter-spacing: 0.5px;
  }
  .brand-panel {
    position: absolute;
    right: 0;
    top: 0;
    width: 300px;
    height: 400px;
    background: linear-gradient(160deg, var(--panel-light), var(--panel-deep));
  }
  .contact-block {
    position: absolute;
    left: 56px;
    top: 268px;
  }
  .contact-name {
    margin: 0 0 34px;
    font-size: 30px;
    font-weight: 700;
    color: var(--brand-navy);
  }
  .contact-list {
    list-style: none;
    margin: 0;
    padding: 0;
  }
  .contact-item {
    font-size: 21px;
    font-weight: 400;
    color: var(--text-blue);
    line-height: 44px;
    letter-spacing: 0.3px;
  }
</style>
</head>
<body>
  <main class="canvas">
    <article class="business-card">
      <p class="brand-name">Qovo International</p>

      <div class="brand-panel" role="img" aria-label="Brand graphic: sweeping blue and orange curved shape"></div>

      <section class="contact-block">
        <h1 class="contact-name">Dennis Marlow</h1>
        <ul class="contact-list">
          <li class="contact-item">+61 427581962</li>
          <li class="contact-item">dennis@qovo.com.au</li>
          <li class="contact-item">P.O. Box 872 Kelvindale QLD 4309</li>
        </ul>
      </section>
    </article>
  </main>
</body>
</html>
```